Bright and beautiful business card for a coach

I'm a personal and business coach based in Perth, Australia. I need a business card that whilst subtle and elegant, will stand out and appeal on a table full of cards.

My business name is Tide Mentoring and the business card must represent the warmth and brightness implied in the name, without being gimmicky. It must have a warmth and appeal and be easy to read.

I prefer clean, minimalist designs.

It must align with the feel of my website and socials: https://www.tidementoring.com.au/
https://www.instagram.com/tidementoringau/
https://www.facebook.com/tidementoringau
Updates

Hi Designers Thank you so much for taking the time to submit designs. I wonder if I could have explained myself a little better. Most of the designs that have been submitted look rather formal and many have quite corporate looking embellishments on them (to my eye). I would like softer, warmer, more organic. I’m open to people playing about and being more abstract, using softer embellishments (e.g the line drawing flowers and grasses I’ve used in my socials) incorporating other colours from my palette or like the social icons in my email signature (in PDF), perhaps playing with size/oversize, playing with the bleed. Please don’t be constrained by what I’ve already done, it merely needs to compliment. I’m sorry if I’m not using the right words or have led you astray. I’m no designer, but I’ve done my website, socials, email signature etc all myself (my logo was a design contest) and I was really hoping for my business card to be something more creative than I could have made with a template. Reminder: No black cards/sides please. Thank you 😊

Target Market(s)

Individuals, most likely but not all female. Creative thinkers. Likely professionals.

Industry/Entity Type

Business & Personal Coach

Contact Information for Business Card

(Tide Mentoring Logo) Name: Maren Delsby; Title: Business & Personal Coach; Phone number: +61 (0)438 915307; Email: maren@tidementoring.com.au; Website: https://tidementoring.com.au; Social icons for Facebook, Instagram & LinkedIn: @tidementoringAU. Optional strapline: "A thinking partner to help you cut through the noise"

Font styles to use
Sans Serif

Colors
00AB8E
00BBA5
67D7C9
C6EFE9
E9F9F6
59FF00
82FF00
B8FF75
E3FFCB
F4FFEA
FFC000
F8CF3A
FAE287
FDF2CF
FEFAEE

Requirements
Must have
• Must align with feel of my website and socials. Must have a pop of #FFC000 (possibly whole of one side, or at least a block). Bright or white background. Easy to read.
Nice to have
• Possibly incorporate the sunshine/grass picture I have used in website and socials - will upload.
Should not have
• Must not be black or dark. Not impersonal or corporate looking.

```html
<!DOCTYPE html>
<html lang="en">
<head>
<meta charset="utf-8">
<title>Tide Mentoring – Business Card</title>
<link rel="stylesheet" href="https://fonts.googleapis.com/css2?family=Lato:wght@400;700&display=swap">
<style>
  :root {
    --page: #ffffff;
    --sun-gold: #ffc000;
    --sun-amber: #fbb51a;
    --leaf-green: #6bff00;
    --grass-deep: #3f7a1c;
    --grass-mid: #8fb33a;
    --glow: #f6c94a;
    --blush: #f2dcd6;
    --ink-light: #ffffff;
  }
  * { margin: 0; padding: 0; box-sizing: border-box; }
  html, body {
    width: 1200px; height: 902px; overflow: hidden;
    background: var(--page);
    font-family: "Lato", sans-serif;
  }
  .sheet { position: relative; width: 1200px; height: 902px; }
  .card {
    position: absolute; top: 292px;
    width: 523px; height: 328px; overflow: hidden;
  }
  .card--front { left: 75px; }
  .card--back { left: 615px; background: var(--leaf-green); }

  .front-photo {
    position: absolute; inset: 0;
    background:
      radial-gradient(circle at 62% 8%, var(--glow) 0%, rgba(246,201,74,0) 40%),
      radial-gradient(circle at 95% 10%, var(--blush) 0%, rgba(242,220,214,0) 25%),
      linear-gradient(180deg, var(--grass-mid) 0%, #6f9a2a 45%, var(--grass-deep) 100%);
  }
  .front-disc {
    position: absolute; left: 42px; top: -55px;
    width: 440px; height: 440px; border-radius: 50%;
    background: rgba(255, 192, 0, 0.72);
  }
  .brand-name {
    position: absolute; left: 0; right: 0; top: 138px;
    text-align: center; color: var(--ink-light);
    font-weight: 400; font-size: 40px; letter-spacing: 6px;
    text-transform: uppercase;
  }

  .sun-mark { position: absolute; left: 0; top: 0; width: 215px; height: 328px; }

  .contact {
    position: absolute; left: 239px; top: 32px;
    color: var(--ink-light); font-size: 19px; line-height: 27px;
  }
  .contact a { color: inherit; text-decoration: none; display: block; }
  .social { display: flex; align-items: center; gap: 6px; margin-top: 4px; }
  .social-dot {
    width: 26px; height: 26px; border-radius: 50%;
    border: 1.5px solid var(--ink-light);
  }
  .social-handle { margin-left: 2px; }

  .person { position: absolute; left: 239px; top: 235px; color: var(--ink-light); }
  .person-name { font-size: 38px; font-weight: 400; line-height: 42px; }
  .person-title { font-size: 14px; line-height: 18px; }
</style>
</head>
<body>
<main class="sheet">
  <section class="card card--front">
    <div class="front-photo" role="img" aria-label="Sunlit close-up photograph of green grass with warm sun glow"></div>
    <div class="front-disc"></div>
    <p class="brand-name">Tide Mentoring</p>
  </section>

  <section class="card card--back">
    <svg class="sun-mark" viewBox="0 0 215 328" role="img" aria-label="Illustrated sun with radiating line rays">
      <defs>
        <radialGradient id="ray-glow" cx="0" cy="164" r="215" gradientUnits="userSpaceOnUse">
          <stop offset="0.35" stop-color="#fbb51a" stop-opacity="0.9"/>
          <stop offset="1" stop-color="#fbb51a" stop-opacity="0.15"/>
        </radialGradient>
      </defs>
      <rect width="215" height="328" fill="url(#ray-glow)"/>
      <circle cx="0" cy="164" r="90" fill="var(--leaf-green)"/>
      <circle cx="0" cy="164" r="85" fill="var(--sun-amber)"/>
    </svg>

    <div class="contact">
      <a href="tel:+61438915307">+61 (0)438 915307</a>
      <a href="mailto:maren@tidementoring.com.au">maren@tidementoring.com.au</a>
      <a href="https://tidementoring.com.au">www.tidementoring.com.au</a>
      <div class="social">
        <span class="social-dot"></span>
        <span class="social-dot"></span>
        <span class="social-dot"></span>
        <span class="social-handle">@tidementoringAU</span>
      </div>
    </div>

    <div class="person">
      <h1 class="person-name">Maren Delsby</h1>
      <p class="person-title">Business &amp; Personal Coach</p>
    </div>
  </section>
</main>
</body>
</html>
```